Investment Advisor E-Newsletter Banner Design

I need a banner designed for an email newsletter that will be sent monthly to clients and prospects. We want to see designs that are elegant and use our logo well. The banner should be 922x150px and should go well with the www.bhtlwest.com website. Should include Logo and email and phone number.

Target Market(s)

High net worth investors

Number of Pages Required

1 page

Requirements
Must have
• logo, place for email (info@bhtlwest.com) and phone number (555-219-0387), colors and design that work well with www.bhtlwest.com website

```html
<!DOCTYPE html>
<html lang="en">
<head>
<meta charset="utf-8">
<title>Bellhart West Advisors – Newsletter Banner</title>
<link rel="stylesheet" href="https://fonts.googleapis.com/css2?family=Roboto:wght@400;500&display=swap">
<style>
  :root {
    --paper: #ffffff;
    --brand-blue: #2b2e85;
    --ink-black: #1b1b1d;
    --divider: #5b5ea6;
    --text: #1f1f1f;
  }
  html, body {
    margin: 0;
    padding: 0;
    overflow: hidden;
    background: var(--paper);
  }
  .banner {
    position: relative;
    width: 1200px;
    height: 195px;
    background: var(--paper);
    overflow: hidden;
    font-family: "Roboto", Arial, sans-serif;
  }
  .banner__swoosh {
    position: absolute;
    inset: 0;
    width: 1200px;
    height: 195px;
  }
  .brand {
    position: absolute;
    left: 48px;
    top: 64px;
    width: 280px;
    height: 68px;
    display: flex;
    align-items: center;
    gap: 14px;
  }
  .brand__dot {
    flex: none;
    width: 40px;
    height: 40px;
    border-radius: 50%;
    background: var(--brand-blue);
  }
  .brand__name {
    font-size: 27px;
    font-weight: 400;
    color: var(--brand-blue);
    line-height: 31px;
  }
  .brand__line {
    display: block;
    white-space: nowrap;
  }
  .divider {
    position: absolute;
    left: 348px;
    top: 56px;
    width: 3px;
    height: 84px;
    background: var(--divider);
  }
  .contact {
    position: absolute;
    left: 377px;
    top: 68px;
    margin: 0;
    padding: 0;
    list-style: none;
    font-size: 18px;
    color: var(--text);
    line-height: 31px;
    white-space: nowrap;
  }
  .contact__label {
    font-weight: 500;
  }
</style>
</head>
<body>
  <header class="banner">
    <svg class="banner__swoosh" viewBox="0 0 1200 195" aria-hidden="true">
      <path fill="var(--ink-black)" d="M735,0 C840,30 930,110 975,195 L1200,195 L1200,0 Z"/>
      <path fill="var(--brand-blue)" d="M765,0 C870,25 960,85 1030,132 C1085,165 1150,128 1200,112 L1200,0 Z"/>
    </svg>

    <div class="brand">
      <span class="brand__dot"></span>
      <span class="brand__name">
        <span class="brand__line">Bellhart West</span>
        <span class="brand__line">Advisors</span>
      </span>
    </div>

    <span class="divider"></span>

    <ul class="contact">
      <li><span class="contact__label">P</span>: 555-219-0387</li>
      <li><span class="contact__label">E</span>: info@bhtlwest.com</li>
    </ul>
  </header>
</body>
</html>
```